Revelation Sanctuary Flyer

We need a flyer for a church seminar that focuses on the Revelation and the sanctuary, it will show images with giants, UFOs maybe some pyramids, sanctuary furniture pieces.

Front Cover, Middle and Back cover. size 8.5 x 11 folded in the middle
The information is in file 1 and file 2.
The other files are examples and ideas for layout.

Target Market(s)

Churches

Requirements
Must have
• 1. Flyer design files have to be print ready.
• 2. Must have appropriate bleed size and safe zone
• PDF, JPEG, PSD, AI, TIFF
Nice to have
• Images of Giants, UFO, Sanctuary building, Pyramids

```html
<!DOCTYPE html>
<html lang="en">
<head>
<meta charset="utf-8">
<title>Revelation &amp; The Great Deception – Seminar Flyer</title>
<link href="https://fonts.googleapis.com/css2?family=Open+Sans:wght@400;600;700;800&display=swap" rel="stylesheet">
<style>
:root{
  --navy:#1d2a33;
  --navy-deep:#15202a;
  --teal:#2f7f8c;
  --teal-light:#4aa3b0;
  --orange:#f0862f;
  --yellow:#f3e01a;
  --white:#ffffff;
  --muted:#c9d3d8;
  --page:#ffffff;
}
*{box-sizing:border-box;margin:0;padding:0}
html,body{width:1200px;height:1000px;overflow:hidden;background:var(--page)}
body{font-family:'Open Sans',Arial,sans-serif;color:var(--white)}
.canvas{position:relative;width:1200px;height:1000px;background:var(--page)}
.abs{position:absolute}
.panel{position:absolute;overflow:hidden}
.photo{position:absolute}

/* ---------- outer spread ---------- */
.back-cover{left:236px;top:28px;width:361px;height:466px;background:var(--navy)}
.front-cover{left:597px;top:28px;width:361px;height:466px;
  background:linear-gradient(180deg,#3c5560 0%,#5d7a80 35%,#4a6268 60%,#2f4036 85%,#3d5234 100%)}
.back-cover .sunset{left:0;top:0;width:361px;height:114px;
  background:linear-gradient(180deg,#6f6a78 0%,#c98a4a 45%,#e2a24a 60%,#5a4634 100%)}
.invite-band{position:absolute;left:0;top:114px;width:361px;height:70px;background:var(--orange);
  display:flex;align-items:center;justify-content:center;text-align:center;
  font-weight:700;font-size:12.5px;line-height:15px;text-transform:uppercase}
.section-head{position:absolute;left:0;width:361px;text-align:center;color:var(--yellow);font-weight:700;font-size:9px;text-transform:uppercase}
.body-small{position:absolute;left:12px;width:340px;font-size:5.6px;line-height:8px;color:var(--muted);text-transform:uppercase}
.body-small em{color:var(--yellow);font-style:italic;font-weight:700}
.question-list{position:absolute;left:12px;top:272px;list-style:none;font-size:6px;line-height:9px;color:var(--muted);text-transform:uppercase}
.question-list li::before{content:"● ";color:var(--white)}
.question-list b{color:var(--yellow)}
.quote{position:absolute;left:240px;top:268px;width:110px;text-align:right;font-size:8px;line-height:10px;color:var(--orange);text-transform:uppercase}
.quote b{font-size:9px}
.location-box{position:absolute;left:12px;top:337px;width:250px;height:100px;border:1.5px solid var(--teal)}
.location-tab{position:absolute;left:0;top:0;width:118px;height:14px;background:var(--teal);
  font-size:7.5px;font-weight:700;line-height:14px;padding-left:6px;clip-path:polygon(0 0,100% 0,92% 100%,0 100%)}
.location-text{position:absolute;left:8px;top:22px;font-size:6px;line-height:8px;color:var(--muted)}
.location-text .church{color:var(--yellow);font-weight:700;font-size:7.5px;line-height:11px}
.location-text .pastor{color:var(--yellow);margin-top:6px}
.location-text .phone b{color:var(--orange)}
.map-area{position:absolute;left:122px;top:6px;width:122px;height:88px;background:linear-gradient(135deg,#22343f,#2a4450)}
.free-stack{position:absolute;display:flex;flex-direction:column}
.free-stack div{border:1.5px solid var(--teal);border-top:none;display:flex;align-items:center;justify-content:center;text-align:center;
  font-size:7.5px;line-height:8px;text-transform:uppercase}
.free-stack div:first-child{border-top:1.5px solid var(--teal)}
.free-stack b{font-weight:700;margin-right:3px}
.streaming{position:absolute;width:361px;text-align:center;font-size:5.6px;letter-spacing:1px;color:var(--muted);text-transform:uppercase}
.streaming b{text-transform:none;color:var(--white)}

.date-tab{position:absolute;left:0;top:0;width:361px;height:42px;background:var(--orange);
  font-weight:700;font-size:12px;text-align:center;line-height:36px;clip-path:polygon(0 0,100% 0,100% 100%,0 82%)}
.date-tab sup{font-size:7px}
.cover-art{left:0;top:42px;width:361px;height:424px;
  background:radial-gradient(ellipse 60% 25% at 60% 12%,#8aa2a8 0%,rgba(138,162,168,0) 70%),
             radial-gradient(ellipse 45% 20% at 55% 58%,#a39176 0%,rgba(163,145,118,0) 70%),
             radial-gradient(ellipse 70% 18% at 50% 92%,#39492e 0%,rgba(57,73,46,0) 80%)}
.church-name{position:absolute;left:100px;top:146px;display:flex;align-items:center;gap:6px;font-size:11px;font-weight:700;color:var(--white)}
.church-name span.dot{width:14px;height:14px;border-radius:50%;background:var(--orange)}
.presents{position:absolute;left:0;top:266px;width:361px;text-align:center;font-size:6.5px;font-weight:700;letter-spacing:1px}
.cover-title{position:absolute;left:0;top:280px;width:361px;text-align:center;color:var(--yellow);font-weight:800;line-height:1}
.cover-title .l1{font-size:34px}
.cover-title .l2{font-size:25.5px;margin-top:4px}

/* ---------- inner spread ---------- */
.inner-left{left:239px;top:505px;width:361px;height:467px;
  background:linear-gradient(180deg,#27414a 0%,#33525a 40%,#2a3e45 70%,#3a3a33 100%)}
.inner-right{left:600px;top:505px;width:362px;height:467px;
  background:linear-gradient(180deg,#2d464e 0%,#3f5659 40%,#5a5646 65%,#3d4d37 100%)}
.sanctuary-head{position:absolute;left:16px;top:70px;color:var(--yellow);font-weight:700;font-size:23px;line-height:35px}
.sanctuary-sub{position:absolute;left:16px;top:140px;font-size:11px;line-height:15px;text-transform:uppercase}
.event-grid{position:absolute;left:16px;top:182px;width:320px;height:123px;border:1px solid var(--teal);display:flex}
.event{flex:1;border-right:1px solid var(--teal);position:relative}
.event:last-child{border-right:none}
.event .thumb{position:absolute;left:3px;top:3px;right:3px;height:68px}
.event .label{position:absolute;left:0;right:0;top:78px;text-align:center;font-size:7.5px;line-height:9px;text-transform:uppercase}
.event .label b{color:var(--yellow);font-weight:700}
.event .when{position:absolute;left:3px;right:3px;top:100px;height:17px;display:flex;align-items:center;font-size:7px;text-transform:uppercase}
.event .when .day{background:var(--orange);height:17px;width:24px;display:flex;align-items:center;justify-content:center;font-size:8.5px;font-weight:600;margin-right:5px}
.event .when sup{font-size:5px}
.family-note{position:absolute;left:16px;top:316px;width:330px;font-size:8px;line-height:12px;font-weight:700;letter-spacing:.4px;text-transform:uppercase}

.future-head{position:absolute;left:245px;top:10px;width:117px;height:17px;border-bottom:1.5px solid var(--teal);
  color:var(--teal-light);font-weight:700;font-size:11px;padding-left:12px}
.topic-list{position:absolute;right:14px;top:34px;width:120px;list-style:none;text-align:right}
.topic-list li{font-size:7px;font-weight:700;line-height:8px;margin-bottom:7.5px}
.topic-list li small{display:block;font-size:4.5px;font-weight:400;color:var(--muted);line-height:6px}
.t-orange{color:var(--orange)}
.t-yellow{color:var(--yellow)}
.t-white{color:var(--white)}
.extras-badge{position:absolute;left:163px;top:33px;width:88px;height:88px;border-radius:50%;background:var(--orange);
  display:flex;flex-direction:column;align-items:center;justify-content:center;transform:rotate(-22deg);
  font-size:6.5px;font-weight:700;line-height:8px;text-transform:uppercase;text-align:center}
.extras-badge span{padding:3px 0;border-bottom:1px solid var(--white);width:66px}
.extras-badge span:last-child{border-bottom:none}
.speaker-tab{position:absolute;left:0;top:224px;width:146px;height:20px;background:var(--orange);
  font-weight:700;font-size:10px;line-height:20px;padding-left:10px;clip-path:polygon(0 0,100% 0,92% 100%,0 100%)}
.speaker-bio{position:absolute;left:47px;top:252px;width:198px;font-size:5.4px;line-height:7.3px}
.speaker-bio b{display:block;color:var(--yellow);font-size:7px;line-height:10px}
.sanctuary-art{left:0;top:60px;width:240px;height:160px;background:radial-gradient(ellipse at 40% 60%,#9e7a4e 0%,rgba(158,122,78,0) 70%)}
</style>
</head>
<body>
<div class="canvas">

  <!-- Back cover -->
  <section class="panel back-cover">
    <div class="photo sunset" role="img" aria-label="Photo of friends sitting on a hillside watching the sunset over a lake"></div>
    <div class="invite-band">We invite you to come as you are and<br>discover hope &amp; lasting peace<br>in these trouble times</div>

    <h3 class="section-head" style="top:197px">Why study Revelation?</h3>
    <p class="body-small" style="top:220px">Blessed is he who reads and those who hear the words of this prophecy, and keep those things which are written in it; for the time is near. <em>Revelation 1:3</em></p>

    <h3 class="section-head" style="top:251px">Find answers to your everyday questions:</h3>
    <ul class="question-list">
      <li>What does the Bible say about <b>the end of the world</b>?</li>
      <li>Were there really <b>giants</b> in the world?</li>
      <li>Are there <b>UFO's</b>?</li>
      <li>Why is there so much <b>pain and suffering</b> in the world?</li>
      <li>Is there <b>life after death</b>?</li>
      <li>Is <b>heaven and hell</b> real?</li>
    </ul>
    <p class="quote">"If you have<br><b>plaguing question,</b><br>submit it and<br>we will answer it..."</p>

    <div class="location-box">
      <div class="location-tab">MEETING LOCATION</div>
      <div class="location-text">
        <div class="church">Bethany Hope Church</div>
        820 Linden Ave<br>Riverton, NY 10990<br>(corner of Linden Ave &amp; Harlow Rd)
        <div class="pastor">Dr. Marcus L. Reed, <span style="color:var(--muted)">Pastor</span></div>
        <div class="phone"><b>Phone :</b> 555-014-2290</div>
      </div>
      <div class="map-area" role="img" aria-label="Street map showing the meeting location"></div>
    </div>
    <div class="free-stack" style="left:262px;top:337px;width:87px">
      <div style="height:25px"><b>FREE</b> ADMISSION</div>
      <div style="height:25px"><b>FREE</b> STUDY GUIDES</div>
      <div style="height:25px"><b>FREE</b> BOOKS</div>
      <div style="height:25px;flex-direction:column"><b>FREE</b>HEALTH MATERIALS</div>
    </div>
    <p class="streaming" style="top:449px">Streaming live at: <b>www.bethanyhope.org/resources/watch-us-live</b></p>
  </section>

  <!-- Front cover -->
  <section class="panel front-cover">
    <div class="photo cover-art" role="img" aria-label="Montage of a flying saucer in a stormy sky, a man with raised arms, pyramids, a giant and standing stones"></div>
    <div class="date-tab">COMING MAY 19<sup>TH</sup> - JUNE 2<sup>ND</sup>, 2018</div>
    <div class="church-name"><span class="dot"></span>Bethany Hope Church</div>
    <p class="presents">PRESENTS</p>
    <h1 class="cover-title"><div class="l1">REVELATION &amp;</div><div class="l2">THE GREAT DECEPTION</div></h1>
    <p class="streaming" style="top:449px">Streaming live at: <b>www.bethanyhope.org/resources/watch-us-live</b></p>
  </section>

  <!-- Inner left -->
  <section class="panel inner-left">
    <div class="photo" style="left:0;top:0;width:361px;height:467px;background:radial-gradient(ellipse 50% 22% at 70% 10%,#6f8890 0%,rgba(111,136,144,0) 75%),radial-gradient(ellipse 45% 25% at 40% 85%,#6b6350 0%,rgba(107,99,80,0) 75%)" role="img" aria-label="Flying saucer over a man standing before pyramids"></div>
    <h2 class="sanctuary-head">GODS WAY IS<br>IN THE SANCTUARY...</h2>
    <p class="sanctuary-sub">The Bible provides solid answers<br>to all your questions</p>
    <div class="event-grid">
      <div class="event">
        <div class="thumb" role="img" aria-label="City skyline at sunset" style="background:linear-gradient(180deg,#c99a5a,#4a4338)"></div>
        <p class="label">Opening Day!<br><b>Intro to Revelation!</b></p>
        <div class="when"><span class="day">SAT</span>MAY 19<sup>TH</sup>&nbsp;| 11:00AM</div>
      </div>
      <div class="event">
        <div class="thumb" role="img" aria-label="Lit marquee letters on a dark background" style="background:linear-gradient(180deg,#3b2d22,#7a5a3a)"></div>
        <p class="label"><b>Ooparts!</b></p>
        <div class="when"><span class="day">SAT</span>MAY 19<sup>TH</sup>&nbsp;| 07:00PM</div>
      </div>
      <div class="event">
        <div class="thumb" role="img" aria-label="Giant in a forest" style="background:linear-gradient(180deg,#4e5c3c,#2c3424)"></div>
        <p class="label">Sunday Night<br><b>The Giants</b></p>
        <div class="when"><span class="day">SUN</span>JUL 30<sup>TH</sup>&nbsp;| 07:00PM</div>
      </div>
    </div>
    <p class="family-note">We invite you to bring the whole family and discover how Bible prophecy is relevant to our times.</p>
    <p class="streaming" style="top:450px">Streaming live at: <b>www.bethanyhope.org/resources/watch-us-live</b></p>
  </section>

  <!-- Inner right -->
  <section class="panel inner-right">
    <div class="photo sanctuary-art" role="img" aria-label="Sanctuary tabernacle, furniture pieces, a couple walking and standing stones"></div>
    <div class="future-head">FUTURE TOPICS</div>
    <div class="extras-badge"><span>Inspirational singing</span><span>Nightly quizzes</span><span>Health topics</span></div>
    <ul class="topic-list">
      <li class="t-orange">Chariots of the Gods<small>MON/ MAY 21/ 07:00PM</small></li>
      <li class="t-yellow">The Great Disappointment<small>TUES/ MAY 22 / 07:00PM</small></li>
      <li class="t-white">Sanctuary Furniture<small>WED/ MAY 23/ 07:00PM</small></li>
      <li class="t-orange">Israel, Evangelic &amp;<br>Sanctuary Rebuilding<small>FRI/ MAY 25/ 07:00PM</small></li>
      <li class="t-yellow">Futurism<small>SAT/ MAY 26/ 11:00AM</small></li>
      <li class="t-white">Summary<small>SAT/ MAY 26/ 07:00PM</small></li>
      <li class="t-orange">Final Deception<small>SUN/ MAY 27/ 07:00PM</small></li>
      <li class="t-yellow">Mark of the Beast &amp;<br>The 7 Last Plagues<small>MON/ MAY 28/ 07:00PM</small></li>
      <li class="t-white">The Woman in Red<small>TUES/ MAY 29/ 07:00PM</small></li>
      <li class="t-orange">Crying Loud in the Rain<small>WED/ MAY 30/ 07:00PM</small></li>
      <li class="t-yellow">The Millennium<small>FRI/ JUNE 1/ 07:00PM</small></li>
      <li class="t-white">The New Jerusalem<small>SAT/ JUNE 2/ 11:00AM</small></li>
    </ul>
    <div class="speaker-tab">MEET OUR SPEAKER</div>
    <p class="speaker-bio"><b>Daniel Whitfield</b>presents Daniel and Revelation with simple wisdom, understanding and vivid illustrations that all ages can comprehend. He believes by knowing the events outlined in God's word, will prepare people to stand in the last days, an help them avoid the pitfalls that Satan has laid for mankind. Prophecy lets us know where we came from and where we are going. So come out and hear God's final message to the last generation.</p>
    <div class="free-stack" style="left:262px;top:354px;width:86px">
      <div style="height:25px"><b>FREE</b> ADMISSION</div>
      <div style="height:25px"><b>FREE</b> STUDY GUIDES</div>
      <div style="height:25px"><b>FREE</b> BOOKS</div>
      <div style="height:24px;flex-direction:column"><b>FREE</b>HEALTH MATERIALS</div>
    </div>
  </section>

</div>
</body>
</html>
```